Northfield Energy Product Distribution Brochure

We are looking to have our current brochure for our customers completely redesigned...the idea is to present the relevant information in an attractive way . Our website is northfieldenergy-example.com where you can find more information about us. We have included a file with a rough idea of the page order and what each should include but feel free to adapt based on design. The example provided is only for context and doesnt have to be maintained. We will be using the brochure both digitally and in print form. As long as it reads easily and is eye catching, the design can be horizontal or vertical.Final deliverable should be indesign file.

"Our Brands" page: should be limited to one page (space being enough) where it has the header for each one (for example diesel generators) space for one or two lines of text and then the corresponding logos for each of the five categories
Updates

For those asking: the "our brands" page should be a single page layout where there is a header with the corresponding section and space for maybe one line of text followed by the two logos for that category. Each of the product pages should be similar in fashion to the one in the document attached: a photo of the product with some white space and space for the text to be included. We will be posting additional examples today

Target Market(s)

We want to present it to customers both digitally and in print so they can see our products

Industry/Entity Type

Power Generation

Font styles to use
Serif

Requirements
Must have
• Eye catching and able to present the information in a presentable fashion. Rest is up to you.
Nice to have
• Should incorporate the colors of our logo but can also add other depending on design

```html
<!DOCTYPE html>
<html lang="en">
<head>
<meta charset="utf-8">
<title>Northfield Energy – Distributor Program Guide</title>
<link rel="stylesheet" href="https://fonts.googleapis.com/css2?family=Michroma&family=Orbitron:wght@900&display=swap">
<style>
  :root {
    --page-bg: #e9e9e7;
    --brand-yellow: #ffe600;
    --brand-gold: #e8b21a;
    --brand-navy: #2e2f86;
    --brand-grey: #4a4641;
    --photo-light: #d9d3c9;
    --photo-mid: #8f867a;
    --photo-dark: #3a342d;
    --white: #ffffff;
  }
  * { margin: 0; padding: 0; box-sizing: border-box; }
  html, body {
    width: 1200px; height: 960px; overflow: hidden;
    background: var(--page-bg);
  }
  .brochure-cover {
    position: absolute; left: 80px; top: 100px;
    width: 1040px; height: 760px; overflow: hidden;
    box-shadow: 0 10px 30px rgba(0,0,0,0.18);
  }
  .cover-art { position: absolute; inset: 0; width: 100%; height: 100%; }
  .brand-lockup {
    position: absolute; left: 560px; top: 90px; width: 320px;
    text-align: center; font-family: "Michroma", sans-serif;
  }
  .brand-mark {
    display: block; width: 44px; height: 44px; margin: 0 auto 18px;
    background: var(--brand-grey);
  }
  .brand-name {
    font-size: 20px; letter-spacing: 1px; color: var(--brand-grey);
    white-space: nowrap;
  }
  .brand-tagline {
    margin-top: 4px; font-size: 8px; letter-spacing: 5px;
    color: var(--brand-grey); white-space: nowrap;
  }
  .cover-title {
    position: absolute; left: 420px; top: 470px;
    transform: rotate(-6deg); transform-origin: left top;
    line-height: 0.95;
  }
  .cover-title .title-line {
    display: block; font-family: "Michroma", sans-serif;
    font-size: 44px; color: transparent;
    -webkit-text-stroke: 1.4px var(--white);
    letter-spacing: 1px;
  }
  .cover-title .title-accent {
    display: block; font-family: "Orbitron", sans-serif; font-weight: 900;
    font-size: 46px; color: var(--brand-gold); letter-spacing: 3px;
    margin-left: 12px; margin-top: -6px;
  }
</style>
</head>
<body>
  <section class="brochure-cover">
    <svg class="cover-art" viewBox="0 0 1040 760" xmlns="http://www.w3.org/2000/svg">
      <defs>
        <linearGradient id="engineTone" x1="0" y1="0" x2="1" y2="1">
          <stop offset="0" stop-color="var(--photo-light)"/>
          <stop offset="0.45" stop-color="var(--photo-mid)"/>
          <stop offset="1" stop-color="var(--photo-dark)"/>
        </linearGradient>
      </defs>
      <rect class="engine-photo" role="img" aria-label="Sepia-toned photograph of a diesel generator engine with turbocharger, pipes and side grille" width="1040" height="760" fill="url(#engineTone)"/>
      <polygon class="logo-panel" points="340,0 880,0 930,160 640,330" fill="var(--white)" opacity="0.93"/>
      <polygon class="corner-accent" points="790,0 1040,0 1040,130" fill="var(--brand-yellow)"/>
      <polygon class="side-accent" points="1040,190 1040,500 830,330" fill="var(--brand-gold)" opacity="0.85"/>
      <polygon class="shadow-band" points="0,470 440,760 300,760 0,560" fill="#1f1c19" opacity="0.45"/>
      <line class="gold-stripe" x1="0" y1="430" x2="480" y2="760" stroke="var(--brand-gold)" stroke-width="6"/>
      <polygon class="navy-band" points="0,580 300,760 200,760 0,650" fill="var(--brand-navy)"/>
    </svg>

    <div class="brand-lockup">
      <span class="brand-mark"></span>
      <div class="brand-name">NORTHFIELD ENERGY</div>
      <div class="brand-tagline">THE GENERATOR COMPANY</div>
    </div>

    <h1 class="cover-title">
      <span class="title-line">DISTRIBUTOR</span>
      <span class="title-line">PROGRAM</span>
      <span class="title-accent">GUIDE</span>
    </h1>
  </section>
</body>
</html>
```